VelmarisHub needs some a graphic design ASAP. Visit https://velmarishub.com/Home/About/ to get a feel for our current design. We need a visually pleasing way to add the information in the files attached to what already exists (the new sections are Reach, Discretion, and Heart).

This can either be a graphic with the information at the bottom or a redesign of the landing page. We'll accept whatever we like most.

I've attached some stock photos that I own / like. Feel free to use these directly or for inspiration. Icons are OK too. These are just an example.

```html
<!DOCTYPE html>
<html lang="en">
<head>
<meta charset="utf-8">
<title>VelmarisHub – About</title>
<link rel="stylesheet" href="https://fonts.googleapis.com/css2?family=Open+Sans:wght@400;600;700;800&family=Arimo:wght@400&display=swap">
<style>
:root{
  --pink:#e8197a;
  --blue:#2bb5e6;
  --pink-soft:#f6bfd8;
  --blue-soft:#bfe6f6;
  --ink:#2e2e2e;
  --line:#d9d9d9;
  --panel:#ffffff;
  --band:#f4f4f4;
  --page:#fbfbfb;
  --footer:#2b2f34;
  --chrome:#f0f0f0;
  --arrow:#333333;
}
*{box-sizing:border-box;margin:0;padding:0}
html,body{width:1200px;height:1051px;overflow:hidden;background:var(--page);font-family:"Open Sans",Arial,sans-serif;color:var(--ink)}
.canvas{position:relative;width:1200px;height:1051px}

.browser-bar{position:absolute;left:0;top:0;width:1200px;height:50px;background:var(--chrome);border-bottom:1px solid #c8c8c8}
.address{position:absolute;left:0;top:14px;width:1016px;height:30px;background:#fff;border:1px solid #b9b9b9;font:17px "Arimo",Arial,sans-serif;color:#555;padding:4px 2px}
.address .tools{position:absolute;right:10px;top:4px;color:#888;font-size:16px}
.search{position:absolute;left:1024px;top:14px;width:176px;height:30px;background:#fff;border:1px solid #b9b9b9;font:italic 16px "Arimo",Arial,sans-serif;color:#777;padding:4px 0 0 10px}
.search .mark{display:inline-block;width:20px;height:20px;background:#4a7fe0;vertical-align:-4px;margin-right:6px}

.card{position:absolute;background:var(--panel);border:1px solid var(--line);border-radius:4px}
.intro{left:75px;top:52px;width:1065px;height:236px;border-top:none;border-radius:0 0 4px 4px}
.intro h2{position:absolute;top:8px;width:100%;text-align:center;font-size:22px;font-weight:700;color:#333}
.steps{position:absolute;left:22px;top:60px;width:1025px;height:133px;border:1px solid #c9c9c9;border-radius:10px;background:linear-gradient(#fff 60%,#ececec);display:flex}
.step{position:relative;border-right:1px solid #cfcfcf;display:flex;flex-direction:column;align-items:center;padding-top:20px;font-size:18px;color:#444}
.step:last-child{border-right:none}
.step-icon{width:60px;height:60px;border-radius:8px;margin-bottom:12px}
.tone-mix{background:linear-gradient(135deg,var(--blue-soft),var(--pink-soft))}
.tone-blue{background:linear-gradient(135deg,var(--blue-soft),#9fd8f0)}
.tone-pink{background:linear-gradient(135deg,var(--pink-soft),#f2a6c8)}
.step .ast{color:var(--pink)}
.next{position:absolute;right:-18px;top:36px;width:35px;height:35px;z-index:2}
.note{position:absolute;left:42px;top:204px;font:14px "Arimo",Arial,sans-serif;color:var(--pink)}

.about{left:75px;top:332px;width:1065px;height:209px}
.band{background:var(--band);border-bottom:1px solid var(--line);border-radius:4px 4px 0 0}
.about .band{height:59px;padding:14px 0 0 26px;font-size:23px;font-weight:800;letter-spacing:-1px;color:#1f1f1f}
.about .band span{color:var(--pink)}
.about p{font:19.5px/25px "Arimo",Arial,sans-serif;color:#222;margin:13px 30px 0 34px}
.about p+p{margin-top:12px}

.feature{top:588px;width:342px;height:324px;text-align:center}
.feature .band{height:60px;padding:15px 0 0 26px;text-align:left;font-size:21px;font-weight:700;color:#111}
.feature-art{width:140px;height:122px;margin:23px auto 0;border-radius:10px}
.feature p{font-size:17px;line-height:22px;color:#222;margin-top:17px}
.f-discretion{left:75px}.f-reach{left:437px}.f-heart{left:799px}

.site-footer{position:absolute;left:0;top:940px;width:1200px;height:111px;background:var(--footer);text-align:right;padding:37px 82px 0 0;font:23px "Arimo",Arial,sans-serif;color:#eee}
.site-footer a{color:var(--pink);text-decoration:underline}
.site-footer .copy{display:block;padding-right:205px;margin-top:2px}
</style>
</head>
<body>
<div class="canvas">
  <div class="browser-bar">
    <div class="address">About/<span class="tools">▿ ↻</span></div>
    <div class="search"><span class="mark"></span>▾ Seekly</div>
  </div>

  <section class="card intro">
    <h2>KNOW SOMEONE SINGLE?</h2>
    <div class="steps">
      <div class="step" style="width:202px">
        <div class="step-icon tone-mix" role="img" aria-label="Icon: sending a message"></div>
        Send a Message
        <svg class="next" viewBox="0 0 35 35"><circle cx="17.5" cy="17.5" r="17.5" fill="var(--arrow)"/><path d="M14 10 L22 17.5 L14 25" stroke="#fff" stroke-width="4" fill="none"/></svg>
      </div>
      <div class="step" style="width:196px">
        <div class="step-icon tone-mix" role="img" aria-label="Icon: receiving a response"></div>
        Get a Response
        <svg class="next" viewBox="0 0 35 35"><circle cx="17.5" cy="17.5" r="17.5" fill="var(--arrow)"/><path d="M14 10 L22 17.5 L14 25" stroke="#fff" stroke-width="4" fill="none"/></svg>
      </div>
      <div class="step" style="width:247px">
        <div class="step-icon tone-mix" role="img" aria-label="Icon: two people being introduced"></div>
        Make an Introduction
        <svg class="next" viewBox="0 0 35 35"><circle cx="17.5" cy="17.5" r="17.5" fill="var(--arrow)"/><path d="M14 10 L22 17.5 L14 25" stroke="#fff" stroke-width="4" fill="none"/></svg>
      </div>
      <div class="step" style="width:176px">
        <div class="step-icon tone-blue" role="img" aria-label="Icon: clock for waiting"></div>
        Wait
        <svg class="next" viewBox="0 0 35 35"><circle cx="17.5" cy="17.5" r="17.5" fill="var(--arrow)"/><path d="M14 10 L22 17.5 L14 25" stroke="#fff" stroke-width="4" fill="none"/></svg>
      </div>
      <div class="step" style="width:204px">
        <div class="step-icon tone-pink" role="img" aria-label="Icon: collecting a payment"></div>
        <span>Collect! <span class="ast">*</span></span>
      </div>
    </div>
    <div class="note">*(Subject to site rules)</div>
  </section>

  <section class="card about">
    <div class="band">WHAT IS <span>VELMARISHUB</span>?</div>
    <p>VelmarisHub is a marketplace for matchmakers. Single? Post a profile so matchmakers can compete to<br>find your perfect match. Know somebody single? You could get paid for setting them up!</p>
    <p>No algorithms. No profile browsing ad nauseam. Just real human matchmakers. VelmarisHub is online<br>dating for an offline world.</p>
  </section>

  <section class="card feature f-discretion">
    <div class="band">DISCRETION</div>
    <div class="feature-art tone-mix" role="img" aria-label="Illustration: private profile document with a seal"></div>
    <p>Register with a private profile<br>and reveal yourself only to<br>matchmakers you choose.</p>
  </section>

  <section class="card feature f-reach">
    <div class="band">REACH</div>
    <div class="feature-art tone-mix" role="img" aria-label="Illustration: circle of connected people"></div>
    <p>Human matchmakers have friends,<br>family, co-workers and acquaintances.<br>When has an algorithm<br>set you up with its cousin?</p>
  </section>

  <section class="card feature f-heart">
    <div class="band">HEART</div>
    <div class="feature-art tone-mix" role="img" aria-label="Illustration: giving to charity"></div>
    <p>If no matchmakers succeed in finding<br>you a match, your reward<br>will be donated<br>to a charity of your choice.</p>
  </section>

  <footer class="site-footer">
    <a href="#">Terms of Use</a> | <a href="#">Terms of Service</a> | <a href="#">Learn More</a> | <a href="#">Contact</a> | <a href="#">Privacy Policy</a>
    <span class="copy">© 2011-2014 Velmaris Hub, LLC</span>
  </footer>
</div>
</body>
</html>
```